Poem Design for Storytelling Company

Who Are We?
Fenra Studio is a storytelling company that focuses on producing artistic content and delivering immersive experiences to inspire us in discovering our inner utopia.
What is Inner Utopia?
We believe an inner utopia exists within every one of us. It is a state of being where one truly accepts and appreciates the holistic and dualistic nature of the self, others and life as a whole. It is the true acceptance of self, true connections with others, full accountability and ownership of one’s problems and true appreciation of life.
Art Direction:
Negative Space Design is the central theme & focal point of our designs. It is deeply ingrained & firmly rooted in Fenra’s ethos of Wander Toward Quiet Harbor. It is both simple & complex. It represents the journey of self-discovery & actualisation: a deeply personal experience. Negative Space is black & white, two extremes, polar opposites, the Yin and Yang. Yet despite the two opposing contrasts, lies the ultimate reality which is the very heart & soul of Negative Space: Perspective. It is neither wrong nor right nor is it black or white. It is everything, yet nothing.
Deliverable:
We are looking for a designer to create art pieces that will supplement our original poems. We are looking to post these poems on Instagram, we and we aim to give our readers an immersive and emotional experience while reading these poems. Since our poems are fairly long, we anticipate the use of a couple of images for each poems (i.e Each image will cover a coupe of lines).
Please refer below to our poems:
1. How Should I Be?
How should I be?
This is what they told me
To Win, and Not to Lose
To Succeed, and Not to Fail
To Laugh, and Not to Cry
To Fear, and Not to Try
To Be, or Not to Be
For Me, or Not for Me?
Trying to do what I am supposed to do
Hoping to be who I am supposed to be
Fearing to do what I wanted to do
Trapped in my body, I want to be free
Until One Day, I am on My Deathbed
Reflecting and thinking about what I regret
Realizing it was about nothing they said
It was me, who didn’t live the life that I had
For those who still have the chance
Smell the roses, and enjoy the dance
2. Ghost (Please see uploaded files)
Design References:
https://files.plumvault.example/share/7QkxB2nLw9HeZr4TpYcMvD3sJa8UfNbGo?view=open

```html
<!DOCTYPE html>
<html lang="en">
<head>
<meta charset="utf-8">
<title>Ghost — Fenra Studio</title>
<link rel="stylesheet" href="https://fonts.googleapis.com/css2?family=EB+Garamond:wght@400&display=swap">
<style>
  :root {
    --paper: #d8cbc5;
    --shade-dark: #6d6261;
    --shade-light: #d6cac4;
    --plum: #7b6990;
    --plum-band: #786894;
    --plum-deep: #1f1020;
    --plum-glow: #9384a6;
    --title: #c2b5c8;
    --verse: #ffffff;
  }
  * { margin: 0; padding: 0; box-sizing: border-box; }
  html, body { width: 1200px; height: 1200px; overflow: hidden; background: var(--paper); }
  .poem-card {
    position: relative;
    width: 1200px;
    height: 1200px;
    overflow: hidden;
    background: var(--paper);
    font-family: "EB Garamond", Georgia, serif;
    font-variant-ligatures: common-ligatures discretionary-ligatures;
    font-feature-settings: "dlig" 1;
  }
  .side-shade { position: absolute; top: 0; height: 1200px; }
  .side-shade--left {
    left: 0; width: 296px;
    background: linear-gradient(to right, var(--shade-light) 0%, #b6aba6 55%, var(--shade-dark) 100%);
  }
  .side-shade--right {
    left: 899px; width: 301px;
    background: linear-gradient(to right, var(--shade-dark) 0%, #a69d99 40%, var(--shade-light) 100%);
  }
  .cross-vertical {
    position: absolute; left: 485px; top: 0; width: 225px; height: 1200px;
    background: var(--plum);
  }
  .cross-horizontal {
    position: absolute; left: 0; top: 284px; width: 1197px; height: 225px;
    background: linear-gradient(to right,
      var(--plum-band) 0%, #4f3f5e 14%, var(--plum-deep) 24.7%,
      #302236 30%, #4a3a58 38%, #6f5f84 45%, #7a6a8d 55%,
      #4a3a56 64%, #2e2035 71%, var(--plum-deep) 75.5%,
      #352640 80%, #4d3e5b 87%, var(--plum-band) 100%);
  }
  .portrait-area {
    position: absolute; left: 320px; top: 225px; width: 545px; height: 380px;
  }
  .portrait-area svg { display: block; width: 100%; height: 100%; }
  .poem-title {
    position: absolute; left: 37px; top: 336px;
    font-size: 78px; font-weight: 400; line-height: 1;
    color: var(--title); letter-spacing: -0.5px;
  }
  .verse {
    position: absolute; left: 0; top: 668px; width: 1195px;
    text-align: center; color: var(--verse);
    font-size: 22px; line-height: 27.3px;
  }
  .verse span { display: block; }
</style>
</head>
<body>
<main class="poem-card">
  <div class="side-shade side-shade--left"></div>
  <div class="side-shade side-shade--right"></div>
  <div class="cross-vertical"></div>
  <div class="cross-horizontal"></div>

  <div class="portrait-area" role="img" aria-label="Geometric portrait illustration glowing at the centre of the cross">
    <svg viewBox="0 0 545 380" preserveAspectRatio="none" aria-hidden="true">
      <defs>
        <radialGradient id="portraitGlow" cx="50%" cy="45%" r="50%">
          <stop offset="0%" stop-color="#9384a6" stop-opacity="0.95"/>
          <stop offset="55%" stop-color="#85759a" stop-opacity="0.55"/>
          <stop offset="100%" stop-color="#7b6990" stop-opacity="0"/>
        </radialGradient>
      </defs>
      <ellipse cx="272" cy="180" rx="272" ry="190" fill="url(#portraitGlow)"/>
    </svg>
  </div>

  <h1 class="poem-title">Ghost</h1>

  <p class="verse">
    <span>I can teach you how to travel through time.</span>
    <span>It’s simple, let memory and object combine.</span>
    <span>I thought I saved your life, but I was wrong.</span>
    <span>That’s why I’m building you a world out of song.</span>
    <span>And I feel</span>
    <span>Your shirt wet with my tears.</span>
    <span>And your laugh</span>
    <span>Is ringing in my ears.</span>
    <span>I can teach you how to talk to the dead.</span>
    <span>Just clear your mind and let them dance in your head.</span>
    <span>Why are things all moving around on their own?</span>
    <span>I don’t want this ghost to ever leave me alone.</span>
    <span>I still feel</span>
    <span>You with me throughout the years.</span>
    <span>And your voice</span>
    <span>Is telling me not to fear.</span>
  </p>
</main>
</body>
</html>
```